Online ticketing company needs new biz card design

Needing an updated business card to reflect our company, incorporating our existing logo and colour scheme (red, black, white). The design should communicate our modern, online, technology, innovation based company.

Details for card need to include the following:

Name
Position
Telephone and extension number
Mobile number
Email
Web address
Physical and/or postal address

Industry/Entity Type

Business

Font styles to use
Sans Serif

Requirements
Must have
• Clear, bold, eye catching design

```html
<!DOCTYPE html>
<html lang="en">
<head>
<meta charset="utf-8">
<title>Passlane business card – front and back options</title>
<link rel="stylesheet" href="https://fonts.googleapis.com/css2?family=Jost:wght@300;400;700&family=Crimson+Text&display=swap">
<style>
  :root {
    --brand-red: #e31e24;
    --ink: #2b2a29;
    --paper: #ffffff;
    --sheet: #ebebeb;
    --label-grey: #777777;
    --edge-grey: #9a9a9a;
  }
  * { margin: 0; padding: 0; box-sizing: border-box; }
  html, body { width: 1200px; height: 1051px; overflow: hidden; }
  body {
    position: relative;
    background: var(--sheet);
    font-family: "Jost", Arial, sans-serif;
  }
  .sheet-title {
    position: absolute; left: 0; width: 1200px; top: 6px;
    text-align: center; font-size: 19px; font-weight: 300;
    color: var(--label-grey);
  }
  .option-number {
    position: absolute; left: 8px; width: 30px;
    font-size: 46px; font-weight: 300; color: var(--ink);
    line-height: 1;
  }
  .card {
    position: absolute; width: 540px; height: 315px; overflow: hidden;
  }
  .card-front { left: 49px; }
  .card-back { left: 611px; }
  .row-1 { top: 29px; }
  .row-2 { top: 362px; }
  .row-3 { top: 706px; }

  .front-red { background: var(--brand-red); color: var(--paper); }
  .front-white-red { background: var(--paper); color: var(--brand-red); border: 1px solid var(--edge-grey); }
  .front-white-ink { background: var(--paper); color: var(--ink); border: 1px solid var(--edge-grey); }

  .wordmark {
    position: absolute; inset: 0;
    display: flex; align-items: center; justify-content: center; gap: 18px;
    font-weight: 700; font-size: 60px; letter-spacing: 2px;
  }
  .wordmark-dot {
    width: 30px; height: 30px; border-radius: 50%; background: currentColor;
  }

  .back-red { background: var(--brand-red); --arc: var(--paper); }
  .back-ink { background: var(--ink); --arc: var(--brand-red); }
  .back-arc { position: absolute; inset: 0; }
  .back-arc circle { fill: none; stroke: var(--arc); stroke-width: 9; }

  .holder-name {
    position: absolute; left: 45px; top: 126px;
    font-family: "Crimson Text", Georgia, serif;
    font-size: 31px; color: var(--paper); line-height: 1;
  }
  .holder-position {
    position: absolute; left: 46px; top: 166px;
    font-family: "Crimson Text", Georgia, serif;
    font-size: 15px; color: var(--paper); line-height: 1;
  }
  .contact-list {
    position: absolute; left: 295px; top: 130px;
    list-style: none; color: var(--paper);
  }
  .contact-list li {
    display: flex; align-items: center; gap: 10px;
    height: 29px; font-size: 16.5px;
  }
  .contact-icon { width: 18px; height: 18px; flex: none; }
  .contact-icon .disc { fill: var(--paper); }
  .contact-icon .glyph { fill: none; stroke: var(--brand-red); stroke-width: 1.6; stroke-linecap: round; stroke-linejoin: round; }
  .contact-icon .glyph-fill { fill: var(--brand-red); }
  .back-ink .contact-icon .glyph { stroke: var(--ink); }
  .back-ink .contact-icon .glyph-fill { fill: var(--ink); }
</style>
</head>
<body>

<svg width="0" height="0" style="position:absolute" aria-hidden="true">
  <symbol id="icon-mobile" viewBox="0 0 20 20">
    <circle class="disc" cx="10" cy="10" r="10"/>
    <rect class="glyph" x="7" y="4.5" width="6" height="11" rx="1"/>
    <circle class="glyph-fill" cx="10" cy="13.3" r="0.9"/>
  </symbol>
  <symbol id="icon-phone" viewBox="0 0 20 20">
    <circle class="disc" cx="10" cy="10" r="10"/>
    <path class="glyph" d="M6.5 5.5c-1 1-.8 3 1.5 5.5s4.5 2.8 5.5 1.8l.8-.8-2-2-1 .8c-.8-.3-2-1.5-2.3-2.3l.8-1-2-2z"/>
  </symbol>
  <symbol id="icon-mail" viewBox="0 0 20 20">
    <circle class="disc" cx="10" cy="10" r="10"/>
    <rect class="glyph" x="5" y="6.5" width="10" height="7"/>
    <path class="glyph" d="M5 6.5l5 4 5-4"/>
  </symbol>
  <symbol id="icon-web" viewBox="0 0 20 20">
    <circle class="disc" cx="10" cy="10" r="10"/>
    <circle class="glyph" cx="10" cy="10" r="5"/>
    <path class="glyph" d="M5 10h10M10 5c-2 2.8-2 7.2 0 10M10 5c2 2.8 2 7.2 0 10"/>
  </symbol>
  <symbol id="icon-home" viewBox="0 0 20 20">
    <circle class="disc" cx="10" cy="10" r="10"/>
    <path class="glyph-fill" d="M10 4.8l5.2 4.6h-1.6v5H11.2v-3H8.8v3H6.4v-5H4.8z"/>
  </symbol>
</svg>

<div class="sheet-title">front&amp;back</div>

<!-- Option 1 -->
<div class="option-number" style="top:172px">1</div>
<section class="card card-front front-red row-1">
  <div class="wordmark"><span class="wordmark-dot"></span>PASSLANE</div>
</section>
<section class="card card-back back-red row-1">
  <svg class="back-arc" viewBox="0 0 540 315" aria-hidden="true"><circle cx="49" cy="157" r="189"/></svg>
  <div class="holder-name">Name Name</div>
  <div class="holder-position">Position</div>
  <ul class="contact-list">
    <li><svg class="contact-icon"><use href="#icon-mobile"/></svg>123 456 789</li>
    <li><svg class="contact-icon"><use href="#icon-phone"/></svg>123 456 789</li>
    <li><svg class="contact-icon"><use href="#icon-mail"/></svg>info@passlane.com</li>
    <li><svg class="contact-icon"><use href="#icon-web"/></svg>www.passlane.com</li>
    <li><svg class="contact-icon"><use href="#icon-home"/></svg>Address here here here</li>
  </ul>
</section>

<!-- Option 2 -->
<div class="option-number" style="top:507px">2</div>
<section class="card card-front front-white-red row-2">
  <div class="wordmark"><span class="wordmark-dot"></span>PASSLANE</div>
</section>
<section class="card card-back back-ink row-2">
  <svg class="back-arc" viewBox="0 0 540 315" aria-hidden="true"><circle cx="49" cy="157" r="189"/></svg>
  <div class="holder-name">Name Name</div>
  <div class="holder-position">Position</div>
  <ul class="contact-list">
    <li><svg class="contact-icon"><use href="#icon-mobile"/></svg>123 456 789</li>
    <li><svg class="contact-icon"><use href="#icon-phone"/></svg>123 456 789</li>
    <li><svg class="contact-icon"><use href="#icon-mail"/></svg>info@passlane.com</li>
    <li><svg class="contact-icon"><use href="#icon-web"/></svg>www.passlane.com</li>
    <li><svg class="contact-icon"><use href="#icon-home"/></svg>Address here here here</li>
  </ul>
</section>

<!-- Option 3 -->
<div class="option-number" style="top:821px">3</div>
<section class="card card-front front-white-ink row-3">
  <div class="wordmark"><span class="wordmark-dot"></span>PASSLANE</div>
</section>
<section class="card card-back back-red row-3">
  <svg class="back-arc" viewBox="0 0 540 315" aria-hidden="true"><circle cx="49" cy="157" r="189"/></svg>
  <div class="holder-name">Name Name</div>
  <div class="holder-position">Position</div>
  <ul class="contact-list">
    <li><svg class="contact-icon"><use href="#icon-mobile"/></svg>123 456 789</li>
    <li><svg class="contact-icon"><use href="#icon-phone"/></svg>123 456 789</li>
    <li><svg class="contact-icon"><use href="#icon-mail"/></svg>info@passlane.com</li>
    <li><svg class="contact-icon"><use href="#icon-web"/></svg>www.passlane.com</li>
    <li><svg class="contact-icon"><use href="#icon-home"/></svg>Address here here here</li>
  </ul>
</section>

</body>
</html>
```